GHollis Busisness Card

I am an aerospace consultant and at this time only need business cards.

Industry/Entity Type

Business

Contact Information for Business Card

Hollis Partners,LLC
Gerald T. Hollis

348 Birch Hollow Road
Madison AL 35762

256-555-0148 (cell)
256-555-0173 (fax)

geraldhollis@mailbrook.net

```html
<!DOCTYPE html>
<html lang="en">
<head>
<meta charset="utf-8">
<title>Hollis Partners, LLC – Business Card</title>
<link href="https://fonts.googleapis.com/css2?family=Barlow:wght@400;700&display=swap" rel="stylesheet">
<style>
  :root {
    --backdrop: #6f7273;
    --card-white: #ffffff;
    --brand-blue: #1a8fc4;
    --deep-blue: #0c5f86;
    --ink-grey: #4a4c4e;
    --silver-light: #e9ecee;
    --silver-dark: #9ea4a8;
  }
  * { margin: 0; padding: 0; box-sizing: border-box; }
  html, body {
    width: 1200px;
    height: 1000px;
    overflow: hidden;
    background: var(--backdrop);
  }
  .business-card {
    position: absolute;
    left: 150px;
    top: 240px;
    width: 900px;
    height: 520px;
    background: var(--card-white);
    overflow: hidden;
    font-family: "Barlow", Arial, sans-serif;
    box-shadow: 0 10px 30px rgba(0,0,0,0.25);
  }
  .brand-band {
    position: absolute;
    left: 0;
    top: 0;
    width: 900px;
    height: 520px;
  }
  .brand-name {
    position: absolute;
    left: 60px;
    top: 78px;
    color: var(--card-white);
    font-weight: 700;
    font-size: 40px;
    letter-spacing: 0.5px;
  }
  .contact-block {
    position: absolute;
    right: 48px;
    top: 272px;
    text-align: right;
    color: var(--ink-grey);
    font-size: 30px;
    line-height: 42px;
  }
  .person-name {
    color: var(--brand-blue);
    font-weight: 700;
    font-size: 36px;
    letter-spacing: 1px;
    margin-bottom: 6px;
  }
  .label { color: var(--brand-blue); }
  .email { color: var(--brand-blue); }
</style>
</head>
<body>
  <div class="business-card">
    <svg class="brand-band" viewBox="0 0 900 520" aria-hidden="true">
      <defs>
        <linearGradient id="blueSheen" x1="0" y1="0" x2="1" y2="0.4">
          <stop offset="0" stop-color="#0a5a80"/>
          <stop offset="0.35" stop-color="#1a8fc4"/>
          <stop offset="0.55" stop-color="#0d6a94"/>
          <stop offset="0.8" stop-color="#1c94c8"/>
          <stop offset="1" stop-color="#0b5c83"/>
        </linearGradient>
        <linearGradient id="silverRim" x1="0" y1="0" x2="1" y2="0">
          <stop offset="0" stop-color="#e9ecee"/>
          <stop offset="0.5" stop-color="#9ea4a8"/>
          <stop offset="1" stop-color="#e9ecee"/>
        </linearGradient>
      </defs>
      <path d="M0 0 H580 C560 150 380 250 0 250 Z" fill="url(#silverRim)"/>
      <path d="M0 0 H560 C535 135 360 232 0 232 Z" fill="url(#blueSheen)"/>
    </svg>
    <div class="brand-name">Hollis Partners,LLC</div>
    <div class="contact-block">
      <div class="person-name">Gerald T. Hollis</div>
      <div class="address">348 Birch Hollow Road, Madison AL 35762</div>
      <div class="phones"><span class="label">cell:</span> 256-555-0148&nbsp; <span class="label">fax:</span> 256-555-0173</div>
      <div class="email">geraldhollis@mailbrook.net</div>
    </div>
  </div>
</body>
</html>
```